Window Treatment specialists need business card design

We are moving into a new location and want to highlight our expertise and all we have to offer. We are now a Larkmoor Fennick Gallery for customized window treatments. We also offer custom soft treatments i.e drapery, valances, cornices, upholstery, pillows, color design services, outdoor fabrics, and specialize in motorization of hard treatments.

Target Market(s)

Home Owners 30- 55 with annual income $150,000 and up

Industry/Entity Type

Home Improvement

Contact Information for Business Card

We want our location, name, email, website, phone number, fax, business logo, and Larkmoor Fennick logo on the card. Anything else we are open to the design.

Font styles to use
Sans Serif

Requirements
Must have
• location, name, email, website, phone number, fax, business logo, and Larkmoor Fennick logo on the card. Anything else we are open to the design.

```html
<!DOCTYPE html>
<html lang="en">
<head>
<meta charset="utf-8">
<title>Solenne Interiors – Business Card</title>
<link rel="stylesheet" href="https://fonts.googleapis.com/css2?family=Source+Sans+3:wght@400;600;700&display=swap">
<style>
  :root {
    --page: #ffffff;
    --card: #2a2a2a;
    --teal: #9ccfd0;
    --ink: #f4f4f4;
  }
  * { margin: 0; padding: 0; box-sizing: border-box; }
  html, body { width: 1200px; height: 900px; overflow: hidden; background: var(--page); }
  body { position: relative; font-family: "Source Sans 3", "Myriad Pro", sans-serif; color: var(--ink); }

  .card { position: absolute; top: 275px; width: 477px; height: 294px; background: var(--card); }
  .card--front { left: 116px; border-radius: 0 52px 0 52px; }
  .card--back { left: 622px; top: 276px; height: 293px; border-radius: 52px 0 52px 0; text-align: center; }

  .brand { position: absolute; left: 52px; top: 92px; color: var(--teal); font-weight: 600; font-size: 34px; line-height: 1; }
  .brand span { display: block; }

  .person { position: absolute; right: 20px; top: 35px; text-align: right; }
  .person__name { color: var(--teal); font-weight: 700; font-size: 20px; line-height: 1.1; }
  .person__role { font-size: 13.5px; margin-top: 2px; }

  .address { position: absolute; right: 21px; top: 157px; text-align: right; font-size: 13.5px; line-height: 17px; }

  .contact { position: absolute; right: 20px; top: 217px; list-style: none; font-size: 13.5px; line-height: 17.5px; }
  .contact li { display: flex; justify-content: flex-end; align-items: center; gap: 7px; }
  .contact svg { width: 11px; height: 11px; fill: var(--teal); stroke: var(--teal); }

  .services__title { margin-top: 65px; color: var(--teal); font-weight: 700; font-size: 17px; letter-spacing: 0.2px; }
  .services__list { list-style: none; margin-top: 17px; font-weight: 600; font-size: 13.5px; }
  .services__list li { line-height: 26.8px; }
  .dot { display: inline-block; width: 7px; height: 7px; border-radius: 50%; background: var(--teal); margin: 0 6px; vertical-align: middle; }

  .partner { margin-top: 26px; font-weight: 700; font-size: 13.5px; display: flex; justify-content: center; align-items: center; gap: 6px; }
  .partner__mark { width: 12px; height: 12px; border-radius: 50%; background: var(--ink); }
</style>
</head>
<body>
  <section class="card card--front">
    <div class="brand"><span>Solenne</span><span>Interiors</span></div>

    <div class="person">
      <p class="person__name">Marcus Delane</p>
      <p class="person__role">Managing Director</p>
    </div>

    <p class="address">12345, Address Goes Here<br>Country Name, 123456</p>

    <ul class="contact">
      <li>044-123 456 789
        <svg viewBox="0 0 12 12" aria-hidden="true"><path stroke="none" d="M2.5 0.8l2 2-1 1.4c.6 1.4 1.8 2.7 3.3 3.3l1.4-1 2 2-1.2 1.8C5 10.2 1.8 7 .7 2z"/></svg>
      </li>
      <li>info@webname.com
        <svg viewBox="0 0 12 12" aria-hidden="true"><rect x="0.5" y="2" width="11" height="8" stroke="none"/><path d="M0.8 2.4L6 6.6l5.2-4.2" fill="none" stroke="#2a2a2a" stroke-width="1"/></svg>
      </li>
      <li>www.websitename.com
        <svg viewBox="0 0 12 12" aria-hidden="true"><g fill="none" stroke-width="1.4"><rect x="0.8" y="5.5" width="6" height="3.4" rx="1.7" transform="rotate(-45 3.8 7.2)"/><rect x="5.2" y="3.1" width="6" height="3.4" rx="1.7" transform="rotate(-45 8.2 4.8)"/></g></svg>
      </li>
    </ul>
  </section>

  <section class="card card--back">
    <h2 class="services__title">CUSTOM SOFT TREATMENTS</h2>
    <ul class="services__list">
      <li>Drapery<span class="dot"></span>Valances</li>
      <li>Cornices<span class="dot"></span>Upholstery<span class="dot"></span>Pillows</li>
      <li>Color Design Services<span class="dot"></span>Outdoor fabrics</li>
      <li>and Specialize in motorization of hard treatments</li>
    </ul>
    <p class="partner">Larkmoor Fennick Gallery<span class="partner__mark"></span></p>
  </section>
</body>
</html>
```